Blood Testing Health App

We are looking for a graphics designer to create a web app for us so that we may insert it into a health management website system.
For branding purposes we are at www.Veritamed.com and we are revamping our website... Example of new colors attached.
How we work...
We are a blood testing company based in the USA.
We offer a blood testing service nationwide in the USA.
We allow customers to order tests directly from us, visit a lab, have their blood drawn, or submit a urine sample, the lab tests it and they send the results back to our computer system and we share it with the customer.
The benefits of this are the customer does not need to go to the doctor and pay for the doctors visit to order these tests, which save them money. The tests are cheaper than going through the doctor. The customer simply uses us to get the test and the results and they can then take the results to their doctor... this process has saved them money. Others may be interested in regular check ups for blood work etc... and this allows them to do it with out needing a doctor, or if you have no insurance, this is a cheaper option too. We are quicker than a doctor, customers do not need appointments etc.
Hopefully you now have a better understanding as to what we do.
Here is the spec.
The app screen size is 750 px wide by 700 px high. ( A pdf is attached to show where the app is going to go, it is on page 3 of the pdf) The customer will have the ability to scroll… therefore the length of the page can be longer.
The app will consist of the following sections
Entry Page –
This will be the first page the user sees upon opening the app. This will be where they are directed from to the sections of the app discussed below. This needs to be branded for VeritaMed with a modern look.
1 – Order Test (Giving them the ability to purchase a blood test within the app)
2 – VeritaMed Dashboard (A dashboard that has everything they could need to use our service_
How it works Section on entry page – this will be a simple set of graphics showing how the service works. We already have the graphics for this, they do not need to be built again. They are attached to this brief
Basic structure of sections –
Order Test –
This page contains all tests, filed in categories – and Sub categories – Each test needs a link to an Information section – Price – Buy Now – Cart Process
VeritaMed Dashboard –
A page of icons along the top of the app
- My Confirmation
- My Nearest Lab
- My Receipt
- My Orders
- My Account
- My Results
- My Inbox
- Contact Us
Sections in more detail -
Order A Test –
Show all categories/ sub categories – There are 23 categories, 14 sub categories, and within these categories are 300 tests - Here is the information for the categories etc - http://www.veritamed.com/panels.aspx?PanelGroupID=4 Just in case it helps :)
We need to present this in a graphic format that is spacious, modern (quillbox, taskhub web appearance is the direction we are going for) We need it to be clear and not overwhelming to the customer.
Functionality idea…
Customer clicks category/ subcategory and tests appear.
Customer sees small 35 word description. For more information the test opens into a lightbox or expand the container which ever graphic designer believes to be most visually appealing
Buy Now must always be visible, along with price of the test
Buying process explained – Customer clicks buy now –
They are then taken to a Review Order screen ( This contains Order summary and choose payment method – insert payment details )
– Confirm payment –
Confirmation screen appears, thanking them.
They are then taken to the VeritaMed Dashboard...
VeritaMed Dashboard –
"My Confirmation" - Print Confirmation Order (PDF is in brief, we want this web based not a pdf download)
"My Nearest Lab Location" - This does not need to be designed because the web developer has this part under control, but we do need the icon in the dashboard
"My Receipt" - Print receipt - This does not exist in our system yet. So we need to create this from scratch - It will need to have - The test they are purchasing and the amount of the test - The customers name - The order ID - Must provide printer friendly option too
"My Orders" - This will have a list of orders - At the end of each order will be a status update of either "Test results" "Open order"
A graphic table format would be perfect. This will be linked to relevant results if they have been received. I have also attached a version of what the customer currently sees on our website. We know it is nasty ;) We are redesigning... but the information is there for this section to help design it with the right info. If the results are ready it will say in this list.
"Results Ready" will be a link to show those results once the customer has clicked the link, and the results will appear in the app, under the icons. There must be a printer friendly version too.
"My Results" Developer will sort this page out but we need the icon... It will be exactly like my orders but only show test results
"My Account" - This will be a place for them to update their personal information - Name, DOB, Address, Email Address
"My Inbox" - An inbox interface - Our way of contacting the customer for promotions we are running etc – We need a design of how this screen will appear. We also need the icon in the dashboard to have a notification on it if there are messages in the customers inbox. A little red 1, or circle with number of messages in the inbox.
"Customer Service" - This does not need to be designed because the web developer has this part under control, but we do need the icon in the dashboard
Icons appear along the top of app ( example - Mac icons/ iphone app icons) When the customer clicks an icon the content always appears below the icons
Here is more information for the icons and what should appear when each icon is clicked.
Screens to be designed –
Entry Page
Order A Test Page
Review Order Screen/Payment Screen - Show a lightbox that shows payment has been confirmed. Customer clicks close and are on the Confirmation Screen
VeritaMed Dashboard - Screens mentioned in detail above
We can't wait to see your designs!
Please email any questions.
Hi all this is the first time we have used pixel forum and understand the budget was too low for this project. We have now increased the budget to $2,000 and extended the deadline by another week
Hi all we are receiving some really great designs. I just added an example of the space that the web app will be going into... It is called "kelvraapp.pdf"
Hi guys updated the brief. Hopefully this will help with the dashboard part of the design

```html
<!DOCTYPE html>
<html lang="en">
<head>
<meta charset="utf-8">
<title>VeritaMed – Order A Test</title>
<link rel="stylesheet" href="https://fonts.googleapis.com/css2?family=Open+Sans:wght@400;600;700&family=Arimo:wght@700&display=swap">
<style>
  :root {
    --page-bg: #c0c3d5;
    --brand-green: #7aab12;
    --brand-green-dark: #6a9a0a;
    --button-green-top: #8cc11f;
    --button-green-bottom: #6ea30c;
    --orange-top: #ff7a12;
    --orange-bottom: #ff5a00;
    --badge-orange: #ff6a00;
    --price-green: #76b414;
    --buy-blue: #3f8fe0;
    --title-grey: #555a5f;
    --body-grey: #6d7176;
    --icon-grey: #bdbdbd;
    --divider: #e2e2e2;
    --panel-border: #dcdcdc;
    --panel-head: #f1f1f1;
    --white: #ffffff;
  }
  * { box-sizing: border-box; margin: 0; padding: 0; }
  html, body { width: 1054px; height: 1200px; overflow: hidden; }
  body {
    background: var(--page-bg);
    font-family: "Open Sans", Arial, sans-serif;
    position: relative;
  }
  .app {
    position: absolute;
    left: 87px;
    top: 127px;
    width: 880px;
    background: var(--white);
    box-shadow: 0 0 0 1px rgba(0,0,0,0.12);
  }

  /* Header */
  .app-header {
    height: 158px;
    background: var(--brand-green);
    position: relative;
    color: var(--white);
  }
  .order-bar {
    position: absolute;
    left: 25px;
    top: 14px;
    width: 510px;
    height: 41px;
  }
  .category-select {
    position: absolute;
    left: 150px;
    top: 0;
    width: 360px;
    height: 41px;
    border-radius: 0 6px 6px 0;
    background: linear-gradient(var(--orange-top), var(--orange-bottom));
    border: 1px solid #e05200;
    display: flex;
    align-items: center;
    padding-left: 37px;
    font-size: 14px;
    font-weight: 600;
  }
  .category-select .category-value { font-size: 16px; margin-left: 8px; }
  .category-select .select-arrows { position: absolute; right: 16px; top: 12px; }
  .order-label {
    position: absolute;
    left: 0;
    top: 0;
    width: 178px;
    height: 41px;
    background: linear-gradient(var(--button-green-top), var(--button-green-bottom));
    clip-path: polygon(0 0, 158px 0, 178px 50%, 158px 100%, 0 100%);
    border-radius: 6px 0 0 6px;
    display: flex;
    align-items: center;
    padding-left: 21px;
    font-size: 18px;
    font-weight: 600;
    text-shadow: 0 1px 0 rgba(0,0,0,0.2);
  }
  .brand {
    position: absolute;
    right: 28px;
    top: 24px;
    display: flex;
    align-items: center;
    gap: 8px;
    font-size: 22px;
    font-weight: 400;
    color: var(--white);
  }
  .brand-square { width: 12px; height: 12px; background: #b8d97a; }
  .intro {
    position: absolute;
    left: 31px;
    top: 77px;
    width: 770px;
    font-size: 13px;
    line-height: 17px;
  }

  /* Test list */
  .test-list { list-style: none; }
  .test-item {
    position: relative;
    border-top: 1px solid var(--divider);
    padding: 24px 26px 0 77px;
  }
  .test-item:first-child { border-top: 0; }
  .test-item.is-open {
    background: linear-gradient(#ffffff, #f7f7f7);
    padding-bottom: 34px;
  }
  .toggle {
    position: absolute;
    left: 22px;
    width: 34px;
    height: 34px;
    border-radius: 50%;
    background: var(--icon-grey);
    color: var(--white);
    display: flex;
    align-items: center;
    justify-content: center;
    font-family: Georgia, serif;
    font-style: italic;
    font-weight: 700;
    font-size: 17px;
  }
  .toggle.is-close { background: var(--badge-orange); font-style: normal; }
  .test-title {
    font-size: 18px;
    font-weight: 600;
    color: var(--title-grey);
    display: flex;
    align-items: center;
    gap: 11px;
    height: 26px;
  }
  .badge {
    background: var(--badge-orange);
    color: var(--white);
    font-size: 13px;
    font-weight: 600;
    padding: 1px 8px 2px;
    line-height: 19px;
  }
  .test-summary {
    margin-top: 8px;
    width: 600px;
    font-size: 12px;
    line-height: 18px;
    color: var(--body-grey);
    white-space: nowrap;
    overflow: hidden;
  }
  .test-description {
    margin-top: 7px;
    width: 590px;
    font-size: 12px;
    line-height: 18px;
    color: var(--body-grey);
  }
  .purchase {
    position: absolute;
    right: 26px;
    top: 15px;
    width: 137px;
    text-align: right;
  }
  .price {
    font-family: "Arimo", Arial, sans-serif;
    font-weight: 700;
    font-size: 20px;
    color: var(--price-green);
    margin-right: 3px;
    line-height: 24px;
  }
  .buy-now {
    display: block;
    margin-top: 5px;
    height: 31px;
    border-radius: 3px;
    background: var(--buy-blue);
    color: var(--white);
    font-family: "Arimo", Arial, sans-serif;
    font-weight: 700;
    font-size: 16px;
    line-height: 31px;
    text-align: center;
  }
  .row-1 { height: 107px; }
  .row-1 .toggle { top: 35px; }
  .row-2 { height: 353px; }
  .row-2 .toggle { top: 40px; }
  .row-3 { height: 111px; }
  .row-3 .toggle { top: 39px; }
  .row-4 { height: 106px; }
  .row-4 .toggle { top: 35px; }
  .row-5 { height: 110px; }
  .row-5 .toggle { top: 39px; }

  .included {
    margin-top: 20px;
    width: 574px;
    height: 179px;
    border: 1px solid var(--panel-border);
    border-radius: 4px;
    background: var(--white);
    overflow: hidden;
  }
  .included-head {
    background: var(--panel-head);
    border-bottom: 1px solid var(--panel-border);
    height: 29px;
    padding-left: 11px;
    font-size: 13px;
    font-weight: 600;
    line-height: 29px;
    color: #8a8d90;
  }
  .included-body { padding: 9px 11px 0; }
  .included-name {
    font-size: 13px;
    font-weight: 600;
    color: var(--title-grey);
    line-height: 19px;
  }
  .included-text {
    margin-top: 4px;
    font-size: 11.5px;
    line-height: 18px;
    color: var(--body-grey);
  }
</style>
</head>
<body>
  <main class="app">
    <header class="app-header">
      <div class="order-bar">
        <div class="category-select">
          Category: <span class="category-value">Most Common</span>
          <svg class="select-arrows" width="10" height="16" viewBox="0 0 10 16" aria-hidden="true">
            <path d="M5 1 L9 6 H1 Z M5 15 L9 10 H1 Z" fill="#ffffff"/>
          </svg>
        </div>
        <div class="order-label">Order A Test</div>
      </div>
      <div class="brand"><span class="brand-square"></span>VeritaMed</div>
      <p class="intro">You'll find many of VeritaMed blood tests included in the categories below. Click on any of the tests for more information including special notes, recommendations and test details. (Test "Profiles" and "Panels" contain more than one blood test).</p>
    </header>

    <ul class="test-list">
      <li class="test-item row-1">
        <span class="toggle">i</span>
        <h2 class="test-title">Anemia Profile <span class="badge">Recommended</span></h2>
        <p class="test-summary">Anemia occurs when the amount of hemoglobin (found in the red blood cells) drops below normal...</p>
        <div class="purchase"><div class="price">$103.00</div><span class="buy-now">Buy Now</span></div>
      </li>

      <li class="test-item row-2 is-open">
        <span class="toggle is-close">
          <svg width="12" height="12" viewBox="0 0 12 12" aria-hidden="true"><path d="M2 2 L10 10 M10 2 L2 10" stroke="#ffffff" stroke-width="2.2" stroke-linecap="round"/></svg>
        </span>
        <h2 class="test-title">Anti-Coagulation Therapy (PT/INR)</h2>
        <p class="test-description">This blood test is recommended for those individuals who take blood thinners such as Warfarin or Clotavin. This test should be completed monthly or no later than every 3 months if you are on long-term therapy. The results of this test will tell you if you are within accepted range for your treatment. These results need to be reviewed with your healthcare provider.</p>
        <section class="included">
          <h3 class="included-head">Tests Included:</h3>
          <div class="included-body">
            <h4 class="included-name">Prothrombin Time (Protime) and<br>International Normalized Ratio (PT/INR)</h4>
            <p class="included-text">This test is used for evaluation of the extrinsic coagulation (clotting) system; it aids in screening for congenital and acquired deficiencies of factors II, V, VII, X, and fibrinogen.7-9 This test is used clinically for the therapeutic monitoring of the blood thinning drug warfarin (Clotavin®)that is used for anticoagulant therapy.</p>
          </div>
        </section>
        <div class="purchase"><div class="price">$28.00</div><span class="buy-now">Buy Now</span></div>
      </li>

      <li class="test-item row-3">
        <span class="toggle">i</span>
        <h2 class="test-title">Arthritis Profile</h2>
        <p class="test-summary">The Arthritis Profile is a comprehensive panel of blood tests used to screen your blood for the most...</p>
        <div class="purchase"><div class="price">$35.00</div><span class="buy-now">Buy Now</span></div>
      </li>

      <li class="test-item row-4">
        <span class="toggle">i</span>
        <h2 class="test-title">CBC with Differential/Platelet Count <span class="badge">Top Seller</span></h2>
        <p class="test-summary">The complete blood count or CBC test is used as a broad screening test to check for such disorders...</p>
        <div class="purchase"><div class="price">$29.50</div><span class="buy-now">Buy Now</span></div>
      </li>

      <li class="test-item row-5">
        <span class="toggle">i</span>
        <h2 class="test-title">Celiac Disease Profile</h2>
        <p class="test-summary">The Arthritis Profile is a comprehensive panel of blood tests used to screen your blood for the most...</p>
        <div class="purchase"><div class="price">$240.00</div><span class="buy-now">Buy Now</span></div>
      </li>
    </ul>
  </main>
</body>
</html>
```